Birthday Card Designs

We are looking for multiple "Happy Birthday" Card designs. We only require the Front Image of the Card!

The cards are to be fun and joyous.
It can be funny, sweet or a mix.Please make the style current, modern, and clean. Outdated/old-looking designs are not what we are after.

We are awarding $100 per card design. We have set the project at 3 winners, though we will look to increase this to more if we like more designs.

Audience: Men and women
Age: 18+
Rating: Clean and family friendly
Colour Scheme: Bright and eye-catching

NOTE: This is my first brief with Sketch Bazaar, and i have opted not to guarantee that I will acquire a design. If all goes well this round, this will definitely change in the future
Updates

Hi Designers,

This is my first time with Sketch Bazaar, and so I'm unsure as to how impressive the quality of submissions can be. This is why the project is not guaranteed.

If this round goes well i will definitely guarantee in the future....

Thanks:)

Reason: To gain a few more entries, I've extended the deadline. I'm hoping for more illustrated content and cool typography, as opposed to simple graphics:) Thanks!

Target Market(s)

Males and Females

Industry/Entity Type

Crowd

Requirements
Must have
• The text/copy is up to the designer, but must include the word Birthday.
Nice to have
• Clean; Current; Conceptual; Cute; Funny; Sweet
Should not have
• Old Look; Dated Ideas; Ancient colour schemes; bad typography

```html
<!DOCTYPE html>
<html lang="en">
<head>
<meta charset="utf-8">
<title>Keep Calm Birthday Card</title>
<link rel="stylesheet" href="https://fonts.googleapis.com/css2?family=Cabin:wght@600&display=swap">
<style>
  :root {
    --backdrop: #0d0d0d;
    --card-red: #c8002f;
    --ink-white: #f7f7f7;
    --text-shadow: rgba(80, 0, 15, 0.45);
  }
  * { margin: 0; padding: 0; box-sizing: border-box; }
  html, body {
    width: 1200px;
    height: 1000px;
    overflow: hidden;
    background: var(--backdrop);
  }
  .stage {
    position: relative;
    width: 1200px;
    height: 1000px;
    background: var(--backdrop);
  }
  .card {
    position: absolute;
    left: 266px;
    top: 44px;
    width: 643px;
    height: 911px;
    background: var(--card-red);
    box-shadow: 0 6px 24px rgba(0, 0, 0, 0.6);
  }
  .crest {
    position: absolute;
    left: 232px;
    top: 52px;
    width: 154px;
    height: 172px;
  }
  .message {
    font-family: "Cabin", "Gill Sans", sans-serif;
    font-weight: 600;
    color: var(--ink-white);
    text-shadow: 1px 2px 2px var(--text-shadow);
  }
  .message__line {
    position: absolute;
    left: 0;
    width: 100%;
    text-align: center;
    line-height: 1;
    white-space: nowrap;
  }
  .message__line--large { font-size: 96px; }
  .message__line--medium { font-size: 74px; }
  .message__line--small { font-size: 60px; }
  .line-keep-calm { top: 253px; }
  .line-and { top: 368px; left: -20px; }
  .line-enjoy { top: 453px; }
  .line-your { top: 566px; left: -12px; }
  .line-birthday { top: 653px; }
  .line-party { top: 766px; left: 10px; }
</style>
</head>
<body>
<main class="stage">
  <section class="card">
    <svg class="crest" viewBox="0 0 154 172" role="img" aria-label="Three white bottles fanned together beneath a small crown of dots">
      <rect x="0" y="0" width="154" height="172" rx="18" fill="#f7f7f7" opacity="0.92"/>
    </svg>
    <h1 class="message">
      <span class="message__line message__line--large line-keep-calm">KEEP CALM</span>
      <span class="message__line message__line--small line-and">AND</span>
      <span class="message__line message__line--large line-enjoy">ENJOY</span>
      <span class="message__line message__line--medium line-your">YOUR</span>
      <span class="message__line message__line--large line-birthday">BIRTHDAY</span>
      <span class="message__line message__line--medium line-party">PARTY!</span>
    </h1>
  </section>
</main>
</body>
</html>
```